Solar Carport

Kestrelmoor renewables is looking for a flyer promoting our solar carport design in Alberta, BC and Saskatchewan. We call it the Lanternshed. We have specific color pallet. Should be flashy, endorse local manufacturing, and the over all design should have a green feel to it. We would also like to add this to our website. We will offer this design in steel and wood beam frame.

```html
<!DOCTYPE html>
<html lang="en">
<head>
<meta charset="utf-8">
<title>Kestrelmoor Renewables – Solar Carport Flyer</title>
<link rel="stylesheet" href="https://fonts.googleapis.com/css2?family=Open+Sans:wght@600;700;800&family=Arimo:wght@400;500&display=swap">
<style>
  :root {
    --page-bg: #e6e7e8;
    --leaf-green: #6abf45;
    --leaf-green-light: #86cf62;
    --deep-green: #47a13a;
    --navy: #233a7b;
    --royal: #3b55a6;
    --ink: #111111;
    --black: #0c0c0c;
    --white: #ffffff;
    --sky: #5f7f95;
    --ground: #2b2b2b;
    --timber: #c9802f;
  }
  * { margin: 0; padding: 0; box-sizing: border-box; }
  html, body { width: 1200px; height: 1000px; overflow: hidden; }
  body { background: var(--page-bg); position: relative; font-family: "Open Sans", sans-serif; }

  .flyer {
    position: absolute; left: 263px; top: 22px;
    width: 675px; height: 955px;
    background: var(--leaf-green);
  }
  .flyer > * { position: absolute; }

  .brand-box {
    left: 7px; top: 6px; width: 164px; height: 122px;
    background: var(--white);
    display: flex; flex-direction: column; align-items: center; justify-content: center; gap: 10px;
  }
  .brand-dot { width: 34px; height: 34px; border-radius: 50%; background: var(--royal); }
  .brand-name {
    font-weight: 700; font-size: 17px; line-height: 1.1; text-align: center;
    color: var(--royal); text-transform: uppercase;
  }

  .tagline-band {
    left: 171px; top: 6px; width: 496px; height: 122px;
    background: var(--black);
  }
  .tagline {
    position: absolute; left: 45px; top: 18px;
    font-weight: 700; font-size: 35px; line-height: 41px; color: var(--white); letter-spacing: -0.2px;
  }
  .tagline .accent { color: var(--leaf-green); }
  .tagline-art {
    position: absolute; right: 6px; top: 6px; width: 150px; height: 110px;
    background: radial-gradient(ellipse at center, rgba(106,191,69,0.18), rgba(106,191,69,0) 70%);
  }

  .specialists-band {
    left: 0; top: 136px; width: 675px; height: 44px;
    background: linear-gradient(90deg, var(--leaf-green), var(--leaf-green-light) 50%, var(--leaf-green));
  }
  .specialists {
    position: absolute; left: 55px; top: 4px; width: 567px; height: 36px;
    background: var(--deep-green); color: var(--white);
    font-weight: 700; font-size: 26px; line-height: 36px; text-align: center; letter-spacing: 0.2px;
  }

  .offer-panel {
    left: 7px; top: 181px; width: 660px; height: 135px;
    background: var(--white);
  }
  .offer-tabs { position: absolute; left: 0; top: 6px; width: 660px; height: 70px; display: flex; }
  .offer-tab {
    height: 70px; color: var(--white); font-weight: 700; font-size: 24px;
    display: flex; align-items: center; justify-content: center; letter-spacing: 0.3px;
    border-bottom: 4px solid var(--navy);
  }
  .offer-tab.products { width: 218px; background: var(--navy); }
  .offer-tab.invest { width: 225px; background: var(--royal); }
  .offer-tab.custom { width: 217px; background: var(--navy); }
  .offer-notes { position: absolute; left: 0; top: 84px; width: 660px; height: 44px; display: flex; align-items: center; }
  .offer-note {
    font-family: "Arimo", sans-serif; font-size: 15px; line-height: 19px; color: var(--ink);
    text-align: center; height: 40px; display: flex; align-items: center; justify-content: center;
  }
  .offer-note:nth-child(1) { width: 218px; }
  .offer-note:nth-child(2) { width: 225px; border-left: 3px solid var(--ink); border-right: 3px solid var(--ink); }
  .offer-note:nth-child(3) { width: 217px; }

  .more-band {
    left: 7px; top: 322px; width: 660px; height: 42px;
    background: linear-gradient(180deg, var(--leaf-green-light), var(--deep-green));
  }
  .more-title {
    position: absolute; left: 91px; top: 4px; width: 480px; height: 32px;
    background: var(--white); color: var(--royal);
    font-weight: 800; font-size: 26px; line-height: 32px; text-align: center; letter-spacing: 0.2px;
  }

  .render-top { left: 4px; top: 371px; width: 663px; height: 255px; }
  .render {
    position: absolute; inset: 0;
    background: linear-gradient(180deg, var(--sky) 0%, #8a9ba6 45%, #555 55%, var(--ground) 100%);
  }
  .render.timber-side { clip-path: polygon(0 0, 383px 0, 272px 100%, 0 100%); }
  .render.panel-side {
    clip-path: polygon(391px 0, 100% 0, 100% 100%, 280px 100%);
    background: linear-gradient(180deg, #3a3a3a 0%, #7d8a96 40%, #333 70%, var(--ground) 100%);
  }
  .render-bottom {
    left: 7px; top: 634px; width: 660px; height: 192px;
    background: linear-gradient(180deg, var(--sky) 0%, #9aa6ad 30%, var(--timber) 45%, #6b6b6b 70%, var(--ground) 100%);
  }

  .closing-band {
    left: 0; top: 836px; width: 675px; height: 50px;
    background: var(--black);
    display: flex; align-items: center; justify-content: center; gap: 14px;
  }
  .closing-rule { width: 100px; height: 3px; background: var(--white); }
  .closing-text { color: var(--white); font-weight: 700; font-size: 26px; }

  .contact-bar {
    left: 0; top: 886px; width: 675px; height: 69px;
    background: var(--white);
    display: flex; align-items: center;
  }
  .contact-item { display: flex; align-items: center; gap: 12px; font-family: "Arimo", sans-serif; font-size: 18px; color: var(--ink); }
  .contact-item.phone { margin-left: 52px; line-height: 25px; }
  .contact-item.web { margin-left: 82px; }
  .contact-icon { width: 40px; height: 40px; border-radius: 50%; background: var(--leaf-green); display: flex; align-items: center; justify-content: center; }
</style>
</head>
<body>
  <main class="flyer">
    <div class="brand-box">
      <span class="brand-dot"></span>
      <span class="brand-name">Kestrelmoor<br>renewables</span>
    </div>

    <header class="tagline-band">
      <h1 class="tagline">your #1 choice <span class="accent">in</span><br><span class="accent">renewable energy</span></h1>
      <div class="tagline-art" role="img" aria-label="Soft green decorative accent"></div>
    </header>

    <div class="specialists-band">
      <h2 class="specialists">YOUR RENEWABLE ENERGY SPECIALISTS</h2>
    </div>

    <section class="offer-panel">
      <div class="offer-tabs">
        <div class="offer-tab products">PRODUCTS</div>
        <div class="offer-tab invest">INVESTISEMENT</div>
        <div class="offer-tab custom">CUSTOM</div>
      </div>
      <div class="offer-notes">
        <p class="offer-note">Grid Tie Micro Generation<br>Solar panels - Off Grid</p>
        <p class="offer-note">Solar power systems are<br>more affordabale than ever</p>
        <p class="offer-note">Every system is<br>individually engineered</p>
      </div>
    </section>

    <div class="more-band">
      <h2 class="more-title">MORE THAN JUST SOLAR PANELS</h2>
    </div>

    <div class="render-top">
      <div class="render timber-side" role="img" aria-label="3D render of the Lanternshed wood beam carport frame over parking stalls"></div>
      <div class="render panel-side" role="img" aria-label="3D render of the Lanternshed carport topped with solar panels"></div>
    </div>
    <div class="render-bottom" role="img" aria-label="3D render of a double row Lanternshed timber carport over a parking lot"></div>

    <div class="closing-band">
      <span class="closing-rule"></span>
      <p class="closing-text">We look forward to serving you!</p>
      <span class="closing-rule"></span>
    </div>

    <footer class="contact-bar">
      <div class="contact-item phone">
        <span class="contact-icon">
          <svg width="22" height="22" viewBox="0 0 24 24" aria-hidden="true"><path fill="#fff" d="M6.6 10.8c1.4 2.8 3.8 5.1 6.6 6.6l2.2-2.2c.3-.3.7-.4 1-.2 1.1.4 2.3.6 3.6.6.6 0 1 .4 1 1V20c0 .6-.4 1-1 1C10.6 21 3 13.4 3 4c0-.6.4-1 1-1h3.5c.6 0 1 .4 1 1 0 1.3.2 2.5.6 3.6.1.3 0 .7-.2 1l-2.3 2.2z"/></svg>
        </span>
        <span>403.555.0182<br>780.555.0147</span>
      </div>
      <div class="contact-item web">
        <span class="contact-icon">
          <svg width="24" height="24" viewBox="0 0 24 24" aria-hidden="true" fill="none" stroke="#fff" stroke-width="1.8"><circle cx="12" cy="12" r="9"/><ellipse cx="12" cy="12" rx="4" ry="9"/><path d="M3 12h18M4.5 7.5h15M4.5 16.5h15"/></svg>
        </span>
        <span>https://kestrelmoorrenewables.com/</span>
      </div>
    </footer>
  </main>
</body>
</html>
```